South Florida Real Estate Brokerage Business

The name is HOME CALVINA REAL ESTATE.
The company is a Real estate realty based in Miami.
Is targeted to Latin American clients.
Must express luxury, and efficiency.
Target clients for properties around 250k to a million +.
Calvina means Royal in Latin.
Should communicate safety and knowledge of the product and transaction with a tech edge.

The web design needs to be a Social tool, with Friendlane and other media integration of some sort. Needs to have a Show case place, a Search place (MLS listings) with maps and filters.
Needs to reflect luxury but also mixed with a social edge capable of engaging clients or transition them to communicate with the page.
Include the logo from the uploaded files, feel free to change the color or font per webdesign.
This is a Front en design, layout and graphics.
Possible future programming if approved.
I can receive Quotes for the Code part.

Target Market(s)

Spanish and English speakers living in Latin America and Canada looking for apartments and houses to buy.

Industry/Entity Type

Business

Requirements
Must have
• Search area.
Neighbourhood area.
Could be a blog or news area.
Client registration.
Social Plugin
Nice to have
• Social linking to networks.
Log in with friendlane account.
Friendlane Like.

```html
<!DOCTYPE html>
<html lang="en">
<head>
<meta charset="utf-8">
<title>Home Calvina Real Estate</title>
<link rel="stylesheet" href="https://fonts.googleapis.com/css2?family=Open+Sans:ital,wght@0,400;0,600;0,700;1,400&family=Oswald:wght@500&family=PT+Sans:wght@400&display=swap">
<style>
:root{
  --ink:#222;
  --text:#444;
  --muted:#777;
  --teal:#1b9aa6;
  --teal-dark:#137d88;
  --gold:#c8861a;
  --orange:#f7a823;
  --orange-dark:#f29a12;
  --panel:#ececec;
  --line:#d8d8d8;
  --white:#fff;
  --footer:#efefef;
  --bottom:#2b2b2b;
}
*{box-sizing:border-box;margin:0;padding:0}
html,body{width:892px;height:1200px;overflow:hidden}
body{position:relative;background:var(--white);font-family:"Open Sans",Arial,sans-serif;color:var(--text);font-size:9px}
.abs{position:absolute}
a{color:inherit;text-decoration:none}

/* brand */
.brand{left:110px;top:6px;display:flex;flex-direction:column;align-items:flex-start}
.brand-square{width:44px;height:44px;background:var(--gold);margin-left:40px;margin-bottom:4px}
.brand-name{font-size:19px;font-weight:400;color:#2a3440;letter-spacing:.5px;line-height:20px}
.brand-sub{font-size:10px;font-weight:400;color:#2a3440;letter-spacing:.8px;margin-left:30px}

/* login */
.login{left:514px;top:5px;width:275px}
.login h4{font-size:10px;font-weight:400;color:var(--ink);margin-bottom:5px}
.login .row{display:flex;gap:5px;align-items:center}
.field{height:17px;border:1px solid #ccc;background:#fff;font-size:8px;color:#444;padding:2px 4px}
.btn-grey{height:18px;border:1px solid #ccc;border-radius:3px;background:linear-gradient(#f7f7f7,#dedede);font-size:9px;color:#444;padding:2px 5px}
.login .links{margin-top:4px;font-size:8px;color:var(--teal)}

/* hero */
.hero{left:28px;top:56px;width:834px;height:363px;background:linear-gradient(100deg,#8fcbe0 0%,#3aa6b9 18%,#3f7a3a 35%,#6a8f3a 48%,#e9d28a 62%,#d8b866 75%,#4d8a3a 90%,#7fb15a 100%)}
.sitesearch{left:512px;top:72px;display:flex;gap:4px}
.sitesearch .field{width:236px;height:18px;color:#999}
.sitesearch .btn-grey{height:18px;width:24px;padding:2px 3px}
.nav{left:104px;top:93px;width:681px;height:28px;background:var(--white);display:flex;align-items:center;padding:0 14px}
.nav a{font-size:9.5px;color:#555;margin-right:18px;text-transform:uppercase}
.nav .join{margin-left:auto;margin-right:6px;font-size:9.5px;color:#555}
.soc{width:17px;height:17px;margin-left:3px;border-radius:2px}
.arrow{top:228px}

/* property search */
.ps-tab{left:104px;top:376px;width:98px;height:21px;background:var(--white);color:var(--gold);font-weight:700;font-size:9px;padding:5px 7px}
.ps-panel{left:104px;top:397px;width:681px;height:50px;background:var(--white);box-shadow:0 2px 4px rgba(0,0,0,.15)}
.ps-field{top:12px}
.ps-field label{display:block;font-size:8.5px;color:var(--gold);font-weight:600;margin-bottom:2px}
.select{height:15px;border:1px solid #bbb;background:linear-gradient(#fff,#eee);font-size:8px;color:#333;padding:1px 4px;position:relative}
.select::after{content:"";position:absolute;right:5px;top:5px;border:3px solid transparent;border-top:4px solid #333}
.ps-btn{left:395px;top:17px;width:110px;height:20px;border-radius:4px;background:linear-gradient(#3cb7c3,var(--teal-dark));color:#fff;font-weight:700;font-size:9px;text-align:center;line-height:20px}
.ps-links{left:517px;top:21px;font-size:8.5px;font-weight:600;color:var(--teal)}
.ps-links span{color:#ccc;margin:0 6px}

/* info boxes */
.info{top:469px;height:148px}
.info h3{height:31px;font-size:10.5px;font-weight:700;color:var(--ink);padding:10px 0 0 14px;background:linear-gradient(#f6f6f6,#dcdcdc)}
.info p{font-size:8px;line-height:12.6px;color:#555;padding:7px 14px 0}
.welcome{left:104px;width:288px;background:var(--panel)}
.news{left:393px;width:171px;background:var(--panel);border-left:1px solid #cfcfcf}
.news h3{padding-left:13px}
.news .title{color:var(--gold);font-size:8px;padding:8px 13px 0}
.news p{padding:4px 13px 0}
.news .more{color:var(--gold);font-size:8px;padding:8px 13px 0}
.hood{left:565px;width:220px;background:var(--orange)}
.hood h3{background:linear-gradient(#fbb53d,var(--orange-dark));padding-left:14px}
.hood-map{position:absolute;left:5px;top:46px;width:116px;height:75px;background:#f1ddb0;border-radius:6px 14px 22px 10px}
.hood p{position:absolute;left:121px;top:41px;width:94px;padding:0;color:#fff;font-size:8px;line-height:12.6px}
.shadow-line{left:104px;top:617px;width:681px;height:4px;background:linear-gradient(rgba(0,0,0,.15),transparent)}

/* features */
.feat-line{left:104px;top:671px;width:688px;height:1px;background:var(--line)}
.feat-tab{left:110px;top:645px;width:145px;height:27px;background:#fff;border:1px solid var(--line);border-bottom:none;font-size:11px;font-weight:700;color:var(--ink);padding:6px 0 0 12px}
.card{top:687px;width:150px;height:146px;border:1px solid #ddd;background:#fff;box-shadow:0 1px 2px rgba(0,0,0,.06)}
.card .photo{position:absolute;left:7px;top:7px;width:135px;height:131px;background:linear-gradient(#a8cbe6 0%,#cfe0ee 22%,#b5786a 30%,#e9dcc4 45%,#d8c6a4 70%,#5e8a45 88%,#3f6e32 100%)}

/* newsletter & testimonials */
.sec-title{font-family:"PT Sans",Arial,sans-serif;font-size:16px;color:#333}
.newsletter{left:110px;top:858px;width:290px}
.newsletter .intro{font-style:italic;font-size:8.5px;line-height:13px;color:#555;margin:4px 0 10px}
.newsletter .row{display:flex;gap:8px}
.newsletter .field{width:195px;height:26px;font-style:italic;color:#999;font-size:8.5px;padding:7px 9px;border-color:#ddd}
.newsletter .btn-grey{height:26px;width:62px;font-size:9.5px;text-align:center;padding:6px 0}
.testi{left:479px;top:858px}
.testi-box{left:481px;top:882px;width:213px;height:65px;border:1px solid #ddd;border-radius:3px;background:#fff;font-style:italic;font-size:8.5px;line-height:13px;color:#555;padding:12px 8px;box-shadow:0 1px 3px rgba(0,0,0,.08)}
.testi-nav{left:568px;top:939px;display:flex;gap:2px}
.testi-nav span{width:14px;height:14px;border-radius:50%;border:1px solid #ccc;background:#f3f3f3}
.testi-author{left:708px;top:889px;font-size:9px;color:var(--ink)}
.testi-author b{display:block;font-weight:700}
.testi-author i{color:#666}

/* footer */
.footer{left:0;top:1002px;width:892px;height:150px;background:var(--footer);border-top:1px solid #ddd}
.f-title{font-size:10px;color:#333;text-transform:uppercase}
.quick{left:104px;top:1016px}
.quick ul{list-style:none;position:absolute;top:20px;font-size:8px;color:#555;line-height:17px}
.mail-head{left:269px;top:1019px;width:153px;height:22px;background:#111;color:#fff;font-family:"Oswald",Arial,sans-serif;font-size:13.5px;font-weight:500;text-align:center;line-height:22px}
.mail-text{left:269px;top:1050px;font-size:8.5px;line-height:13px;color:#333}
.mail-field{left:269px;top:1085px;width:148px;height:19px;border:1px solid #ccc;border-radius:10px;background:#fff;font-size:7.5px;color:#555;padding:3px 8px}
.mail-join{left:390px;top:1085px;width:27px;height:19px;border-radius:10px;background:#f06a13;color:#fff;font-weight:700;font-size:7.5px;text-align:center;line-height:19px}
.blog{left:449px;top:1016px;width:160px}
.blog .post{margin-top:6px;font-size:8px;line-height:12px;color:#444}
.blog .date{color:var(--gold);letter-spacing:.8px}
.connect{left:624px;top:1012px}
.connect .icons{display:flex;gap:14px;margin-top:11px}
.connect .icons span{width:22px;height:22px;border-radius:3px}
.plus{left:628px;top:1069px;display:flex;gap:4px;align-items:center}
.plus .box{width:24px;height:14px;border-radius:2px;background:#e8e8e8;border:1px solid #bbb}
.plus .count{font-size:7.5px;border:1px solid #ccc;background:#fff;padding:1px 4px}
.like{left:628px;top:1095px;display:flex;gap:4px;align-items:center;font-size:7.5px;color:#333}
.like .btn{border:1px solid #9aa7c4;background:#eceef5;padding:1px 4px;color:#3b5998;font-size:7.5px}
.like .dot{width:9px;height:9px;background:#3b5998}
.bottom{left:0;top:1152px;width:892px;height:48px;background:var(--bottom)}
.bottom .mini{position:absolute;left:100px;top:8px;color:#caa46a;font-size:9px;line-height:10px}
.bottom .mini i{display:block;width:14px;height:14px;background:#a07a3a;margin:0 0 2px 12px}
.bottom .legal{position:absolute;left:167px;top:16px;font-size:8px;color:#999;line-height:12px}
.bottom .legal b{font-weight:400;color:#ddd;display:block}
</style>
</head>
<body>

<!-- header -->
<div class="abs brand">
  <span class="brand-square"></span>
  <span class="brand-name">HOME CALVINA</span>
  <span class="brand-sub">REAL ESTATE</span>
</div>

<div class="abs login">
  <h4>CLIENT LOGIN</h4>
  <div class="row">
    <div class="field" style="width:112px">Username</div>
    <div class="field" style="width:111px">Password</div>
    <div class="btn-grey">LOGIN</div>
  </div>
  <div class="links">Forgot your password? / Register</div>
</div>

<!-- hero -->
<div class="abs hero" role="img" aria-label="Waterfront Mediterranean villa with palm trees, dock and Miami skyline across turquoise water"></div>
<div class="abs sitesearch">
  <div class="field">MLS ID, Building Name, Address, City, Zip, or Agent Name</div>
  <div class="btn-grey">GO</div>
</div>
<nav class="abs nav">
  <a>Home</a><a>Company</a><a>Associates</a><a>Search Properties</a><a>Marketing and Design</a><a>Contac</a>
  <span class="join">JOIN</span>
  <span class="soc" style="background:#3fb3e0" aria-label="Chirpline"></span>
  <span class="soc" style="background:#3b5998" aria-label="Friendlane"></span>
  <span class="soc" style="background:#f07d1a" aria-label="RSS"></span>
</nav>
<svg class="abs arrow" style="left:107px" width="22" height="34" viewBox="0 0 22 34"><polyline points="18,3 5,17 18,31" fill="none" stroke="#fff" stroke-width="5"/></svg>
<svg class="abs arrow" style="left:764px" width="22" height="34" viewBox="0 0 22 34"><polyline points="4,3 17,17 4,31" fill="none" stroke="#fff" stroke-width="5"/></svg>

<!-- property search -->
<div class="abs ps-tab">PROPERTY SEARCH</div>
<div class="abs ps-panel">
  <div class="abs ps-field" style="left:14px"><label>Location</label><div class="select" style="width:98px">Location</div></div>
  <div class="abs ps-field" style="left:135px"><label>Price</label>
    <div style="display:flex;align-items:center;gap:5px"><div class="select" style="width:50px">Any</div><span style="font-size:8px">to</span><div class="select" style="width:50px">Any</div></div>
  </div>
  <div class="abs ps-field" style="left:273px"><label>Beds</label><div class="select" style="width:50px">Any</div></div>
  <div class="abs ps-field" style="left:331px"><label>Baths</label><div class="select" style="width:50px">Any</div></div>
  <div class="abs ps-btn">PROPERTY SEARCH</div>
  <div class="abs ps-links">Search by MLS #<span>|</span>Advanced Search</div>
</div>

<!-- info boxes -->
<section class="abs info welcome">
  <h3>WELCOME TO HOME CALVINA REAL ESTATE</h3>
  <p>Lorem ipsum dolor sit amet, consectetur adipisicing elit, sed do eiusmod tempor incididunt ut labore et dolore magna aliqua. Ut enim ad minim veniam, quis nostrud exercitation ullamco laboris nisi ut aliquip ex ea commodo consequat. Duis aute irure dolor in reprehenderit in voluptate velit esse cillum dolore eu fugiat nulla pariatur. Excepteur sint occaecat cupidatat non proident, sunt in culpa qui officia deserunt mollit anim id est laborum.</p>
</section>
<section class="abs info news">
  <h3>NEWS</h3>
  <div class="title">Lorem ipsum dolor sit amet</div>
  <p>Lorem ipsum dolor sit amet, consectetur adipisicing elit, sed do eiusmod tempor incididunt ut labore et dolore magna aliqua. Ut enim ad minim veniam, quis nostrud exercitation ullamco laboris.</p>
  <div class="more">Read more...</div>
</section>
<section class="abs info hood">
  <h3>NEIGHBOURHOOD AREA</h3>
  <div class="hood-map" role="img" aria-label="Map of the United States"></div>
  <p>Lorem ipsum dolor sit amet, consectetur adipisicing elit, sed do eiusmod tempor incididunt ut labore et dolore magna aliqua.</p>
</section>
<div class="abs shadow-line"></div>

<!-- featured -->
<div class="abs feat-line"></div>
<div class="abs feat-tab">FEATURE PROPERTY</div>
<div class="abs card" style="left:105px"><div class="photo" role="img" aria-label="Two-storey house with tiled roof, garage and palm trees"></div></div>
<div class="abs card" style="left:280px"><div class="photo" role="img" aria-label="Two-storey house with tiled roof, garage and palm trees"></div></div>
<div class="abs card" style="left:457px"><div class="photo" role="img" aria-label="Two-storey house with tiled roof, garage and palm trees"></div></div>
<div class="abs card" style="left:634px"><div class="photo" role="img" aria-label="Two-storey house with tiled roof, garage and palm trees"></div></div>

<!-- newsletter -->
<section class="abs newsletter">
  <h2 class="sec-title" style="font-weight:400">Newsletter</h2>
  <p class="intro">Lorem ipsum dolor sit amet, consectetur adipisicing elit, sed do eiusmod tempor incididunt ut labore et dolore magna</p>
  <div class="row"><div class="field">Please insert Email and hit Enter</div><div class="btn-grey">Sign Up</div></div>
</section>

<!-- testimonials -->
<h2 class="abs sec-title testi" style="font-weight:400">Testimonials</h2>
<div class="abs testi-box">Lorem ipsum dolor sit amet, consectetur adipisicing elit, sed do eiusmod tempor incididunt ut labore et dolore magna</div>
<div class="abs testi-nav"><span></span><span></span></div>
<div class="abs testi-author"><b>Lorem ipsum</b><i>dolor sit</i></div>

<!-- footer -->
<footer class="abs footer"></footer>
<div class="abs quick">
  <div class="f-title">Quick Links</div>
  <ul style="left:3px"><li>Home</li><li>About Us</li><li>Search Properties</li><li>News</li></ul>
  <ul style="left:96px"><li>BLog</li><li>Testimonials</li><li>Contact</li></ul>
</div>
<div class="abs mail-head">JOIN OUR MAILING LIST</div>
<div class="abs mail-text">Sign up for our e-mail list to<br>receive updates</div>
<div class="abs mail-field">Your e-mail address</div>
<div class="abs mail-join">JOIN</div>

<div class="abs blog">
  <div class="f-title">Blog</div>
  <div class="post"><div class="date">09 April 2012</div>Lorem ipsum dolor sit amet, consectetur adipisicing elit, sed do</div>
  <div class="post"><div class="date">06 April 2012</div>Lorem ipsum dolor sit amet, consectetur adipisicing elit, sed do</div>
  <div class="post"><div class="date">03 April 2012</div>Lorem ipsum dolor sit amet, consectetur adipisicing elit, sed do</div>
</div>

<div class="abs connect">
  <div class="f-title">Connect with us</div>
  <div class="icons">
    <span style="background:#3b5998" aria-label="Friendlane"></span>
    <span style="background:#3fb3e0" aria-label="Chirpline"></span>
    <span style="background:#1f6fa8" aria-label="Linkwork"></span>
    <span style="background:#f07d1a" aria-label="RSS"></span>
  </div>
</div>
<div class="abs plus"><span class="box" aria-label="Plusmark"></span><span class="count">17</span></div>
<div class="abs like"><span class="btn">Like</span><span class="dot"></span><span>2,942 people like this.</span></div>

<div class="abs bottom">
  <div class="mini"><i></i>HOME CALVINA<br>REAL ESTATE</div>
  <div class="legal">Terms of Use | Privacy Policy<b>© 2011 Home Calvina Real Estate .All Rights Reserved</b></div>
</div>

</body>
</html>
```